Adventure Business Cards

Please check out our website for style
Vertical card
Details:
Side 1
Logo
Business name: Kestrel Point Wildland Tours
Name: Colin Warbeck
Role: Director
Email: info@kestrelpointtours.com
Address: PO Box 71, Marlin Cove NSW 2471
Phone: +61 2 5550 1847
Web address: www.kestrelpointtours.com
Side 2
Taking pictures?
A Friendwall and Pixlane logo
Tag us in your pictures with
#kpwildtours
@kpwildtours
www.kestrelpointtours.com
Details:
Side 1
Logo
Name: Colin Warbeck
Role: Director
Phone: +61 2 5550 1847
Side 2
Taking pictures?
#kpwildtours
@kpwildtours

```html
<!DOCTYPE html>
<html lang="en">
<head>
<meta charset="utf-8">
<title>Kestrel Point Wildland Tours – Business Cards</title>
<link href="https://fonts.googleapis.com/css2?family=Open+Sans:wght@400;600&family=Ubuntu:wght@400;500&display=swap" rel="stylesheet">
<style>
  :root {
    --sea-blue: #0a74b0;
    --deep-blue: #06659c;
    --sun-yellow: #f9c923;
    --ink: #1b1b1b;
    --white: #ffffff;
    --backdrop: #e9e9e6;
  }
  * { margin: 0; padding: 0; box-sizing: border-box; }
  html, body {
    width: 1200px; height: 894px; overflow: hidden;
    background: var(--backdrop);
  }
  .canvas { position: relative; width: 1200px; height: 894px; }

  .card {
    position: absolute; top: 103px; width: 393px; height: 687px;
    background: var(--sea-blue); overflow: hidden;
    box-shadow: 0 4px 14px rgba(0,0,0,0.25);
  }
  .card--front { left: 182px; }
  .card--back { left: 625px; }

  .photo { position: absolute; left: 0; top: 0; width: 100%; }
  .photo--bay {
    height: 242px;
    background: linear-gradient(180deg, #b9cfe0 0%, #8fb3cf 30%, #5f7d4a 55%, #3f7f74 75%, #6b6a3f 100%);
  }
  .photo--island {
    height: 254px;
    background: linear-gradient(180deg, #2f7fc0 0%, #6aa6d6 35%, #4e7f63 55%, #2c7fb0 70%, #1d6e9f 100%);
  }

  .brand-mark {
    position: absolute; left: 118px; top: 162px; width: 160px; height: 160px;
    border-radius: 50%; background: var(--ink);
    display: flex; align-items: center; justify-content: center; text-align: center;
    padding: 24px;
    font-family: "Ubuntu", sans-serif; font-weight: 500; font-size: 19px; line-height: 1.2;
    color: var(--white);
  }

  .name-plate {
    position: absolute; left: 15px; top: 345px; width: 363px; height: 74px;
    background: var(--ink); text-align: center;
    font-family: "Open Sans", sans-serif;
  }
  .name-plate__name {
    display: block; margin-top: 6px;
    font-size: 29px; font-weight: 600; letter-spacing: 2.5px; color: var(--white);
  }
  .name-plate__role {
    display: block; margin-top: -3px;
    font-size: 18px; letter-spacing: 2px; color: var(--sun-yellow);
  }

  .contact-panel {
    position: absolute; left: 15px; top: 444px; width: 363px; height: 167px;
    background: var(--sun-yellow);
  }
  .contact-row {
    position: absolute; left: 38px; display: flex; align-items: flex-start;
    font-family: "Ubuntu", sans-serif; font-size: 16.5px; line-height: 21px; color: var(--ink);
  }
  .contact-row svg { width: 22px; height: 20px; margin-right: 18px; flex: none; }
  .contact-row--email { top: 28px; }
  .contact-row--post { top: 61px; }
  .contact-row--phone { top: 114px; }

  .web-band {
    position: absolute; left: 0; width: 100%; height: 53px;
    display: flex; align-items: center; justify-content: center;
    font-family: "Open Sans", sans-serif; font-weight: 600; color: var(--white);
  }
  .web-band--front { top: 626px; background: var(--deep-blue); font-size: 18px; letter-spacing: 1.6px; }
  .web-band--back { top: 611px; background: var(--ink); font-size: 17.5px; letter-spacing: 0.4px; }

  .back-headline {
    position: absolute; left: 0; top: 146px; width: 100%; text-align: center;
    font-family: "Open Sans", sans-serif; font-variant: small-caps;
    font-size: 30px; letter-spacing: 2.5px; color: var(--white);
  }
  .tag-band {
    position: absolute; left: 0; top: 254px; width: 100%; height: 65px;
    background: var(--sun-yellow);
    display: flex; align-items: center; justify-content: center;
    font-family: "Ubuntu", sans-serif; font-size: 21.5px; color: var(--ink);
  }

  .social {
    position: absolute; left: 0; width: 100%; text-align: center;
  }
  .social--pixlane { top: 334px; }
  .social--friendwall { top: 464px; }
  .social__badge {
    width: 86px; height: 86px; margin: 0 auto; border-radius: 50%;
    background: var(--white); color: var(--sea-blue);
    display: flex; align-items: center; justify-content: center;
    font-family: "Ubuntu", sans-serif; font-weight: 500; font-size: 15px;
  }
  .social__handle {
    display: block; margin-top: 12px;
    font-family: "Open Sans", sans-serif; font-size: 18px; letter-spacing: 2.5px; color: var(--white);
  }
</style>
</head>
<body>
<main class="canvas">

  <section class="card card--front" aria-label="Card front">
    <div class="photo photo--bay" role="img" aria-label="Photo of a green island bay with turquoise lagoon and hills"></div>
    <div class="brand-mark">Kestrel Point Wildland Tours</div>

    <div class="name-plate">
      <span class="name-plate__name">Colin Warbeck</span>
      <span class="name-plate__role">Director</span>
    </div>

    <div class="contact-panel">
      <div class="contact-row contact-row--email">
        <svg viewBox="0 0 22 20" aria-hidden="true"><rect x="1" y="4" width="20" height="13" fill="none" stroke="#0a74b0" stroke-width="2"/><path d="M1 4 L11 12 L21 4" fill="none" stroke="#0a74b0" stroke-width="2"/></svg>
        <span>info@kestrelpointtours.com</span>
      </div>
      <div class="contact-row contact-row--post">
        <svg viewBox="0 0 22 20" aria-hidden="true"><path d="M11 20 C6 13 4 10 4 7 A7 7 0 0 1 18 7 C18 10 16 13 11 20 Z" fill="#0a74b0"/><circle cx="11" cy="7" r="2.6" fill="#f9c923"/></svg>
        <span>PO Box 71, Marlin Cove<br>NSW 2471</span>
      </div>
      <div class="contact-row contact-row--phone">
        <svg viewBox="0 0 22 20" aria-hidden="true"><path d="M1 7 Q11 0 21 7 L18 10 L15 7 L7 7 L4 10 Z" fill="#0a74b0"/><rect x="4" y="10" width="14" height="8" rx="1.5" fill="#0a74b0"/><circle cx="11" cy="14" r="2" fill="#f9c923"/></svg>
        <span>+61 2 5550 1847</span>
      </div>
    </div>

    <div class="web-band web-band--front">www.kestrelpointtours.com</div>
  </section>

  <section class="card card--back" aria-label="Card back">
    <div class="photo photo--island" role="img" aria-label="Photo of twin mountain peaks rising from a blue sea"></div>
    <h2 class="back-headline">Taking pictures?</h2>
    <div class="tag-band">Tag us in your pictures with</div>

    <div class="social social--pixlane">
      <div class="social__badge">Pixlane</div>
      <span class="social__handle">#kpwildtours</span>
    </div>
    <div class="social social--friendwall">
      <div class="social__badge">Friendwall</div>
      <span class="social__handle">@kpwildtours</span>
    </div>

    <div class="web-band web-band--back">www.kestrelpointtours.com</div>
  </section>

</main>
</body>
</html>
```